Studying Effectively To Do List

I am looking to design a new "Study To Do List" for High School students (Ages 15 - 18) . This will be printed as an A4 notepad and so should only be a single A4 page.

The Design will need to be professional and look semi-serious but also be appealing to High school students (Ages 15 - 18) and should NOT be gender specific.

I have attached a word document outlining the structure of the page. The space provided should be large enough that people can write in it comfortably.

The notepad will most likely be printed in black and white but I'm also looking at coloured options - colours should be kept to a minimum.

This will be printed professionally and should also include a 3mm bleed.

The design should also include the business logo (included in the word document)

Target Market(s)

High School students (Ages 15 - 18). Both genders

Industry/Entity Type

Education

Font styles to use
Serif
Sans Serif

Requirements
Must have
• Please see the word document attached.
Should not have
• Too much colour

```html
<!DOCTYPE html>
<html lang="en">
<head>
<meta charset="utf-8">
<title>Study To Do List</title>
<link rel="stylesheet" href="https://fonts.googleapis.com/css2?family=Arimo:wght@400;700&display=swap">
<style>
  :root {
    --navy: #1f3a55;
    --orange: #f07a22;
    --ink: #222222;
    --paper: #ffffff;
  }
  html, body { margin: 0; padding: 0; width: 1200px; height: 1200px; overflow: hidden; background: var(--paper); }
  .sheet { display: block; width: 1200px; height: 1200px; font-family: "Arimo", Arial, sans-serif; }
  .page-frame { fill: var(--paper); stroke: var(--navy); stroke-width: 3; }
  .header-band { fill: var(--navy); }
  .accent-line { stroke: var(--orange); stroke-width: 3; }
  .tab { fill: var(--navy); }
  .tab-label { fill: #fff; font-weight: 700; font-size: 15.5px; dominant-baseline: middle; }
  .grid { fill: none; stroke: var(--ink); stroke-width: 1.5; }
  .cell-text { fill: var(--ink); font-size: 15px; dominant-baseline: middle; }
  .brand-name { fill: var(--navy); font-weight: 700; font-size: 26px; text-anchor: middle; dominant-baseline: middle; }
  .brand-dot { fill: var(--orange); }
  .date-label { fill: var(--ink); font-size: 17px; dominant-baseline: middle; }
  .date-line { stroke: var(--ink); stroke-width: 2.5; }
</style>
</head>
<body>
<svg class="sheet" viewBox="0 0 1200 1200" xmlns="http://www.w3.org/2000/svg">
  <!-- Page -->
  <rect class="page-frame" x="205" y="42" width="790" height="1116"/>
  <path class="header-band" d="M205 42 H995 V106 H668 C650 106 642 98 636 86 C630 72 624 61 612 61 H205 Z"/>
  <line class="accent-line" x1="207" y1="64" x2="612" y2="64"/>

  <!-- Brand -->
  <circle class="brand-dot" cx="530" cy="128" r="7"/>
  <text class="brand-name" x="604" y="129">Northway</text>

  <!-- Date -->
  <text class="date-label" x="765" y="136">Date:</text>
  <line class="date-line" x1="812" y1="140" x2="962" y2="140"/>

  <!-- Revision -->
  <g class="section revision">
    <path class="tab" d="M236 174 H392 L410 182 V198 H236 Z"/>
    <text class="tab-label" x="258" y="187">REVISION</text>
    <rect class="grid" x="237" y="198" width="727" height="103"/>
    <path class="grid" d="M237 221 H964 M237 248 H964 M237 277 H964 M595 198 V301"/>
    <text class="cell-text" x="258" y="210">1</text><text class="cell-text" x="622" y="210">5</text>
    <text class="cell-text" x="258" y="234">2</text><text class="cell-text" x="622" y="234">6</text>
    <text class="cell-text" x="258" y="262">3</text><text class="cell-text" x="622" y="262">7</text>
    <text class="cell-text" x="258" y="289">4</text><text class="cell-text" x="622" y="289">8</text>
  </g>

  <!-- Homework -->
  <g class="section homework">
    <path class="tab" d="M236 321 H390 L408 329 V345 H236 Z"/>
    <text class="tab-label" x="258" y="334">HOME WORK</text>
    <rect class="grid" x="237" y="345" width="727" height="300"/>
    <path class="grid" d="M237 366 H964 M237 394 H964 M237 423 H964 M237 450 H964 M237 474 H964 M237 498 H964 M237 525 H964 M237 549 H964 M237 575 H964 M237 599 H964 M237 623 H964"/>
    <text class="cell-text" x="258" y="356">Subject</text><text class="cell-text" x="353" y="356">:</text>
    <text class="cell-text" x="258" y="380">Task</text><text class="cell-text" x="353" y="380">:</text>
    <text class="cell-text" x="258" y="409">Subject</text><text class="cell-text" x="353" y="409">:</text>
    <text class="cell-text" x="258" y="437">Task</text><text class="cell-text" x="353" y="437">:</text>
    <text class="cell-text" x="258" y="463">Subject</text><text class="cell-text" x="353" y="463">:</text>
    <text class="cell-text" x="258" y="486">Task</text><text class="cell-text" x="353" y="486">:</text>
    <text class="cell-text" x="258" y="512">Subject</text><text class="cell-text" x="353" y="512">:</text>
    <text class="cell-text" x="258" y="538">Task</text><text class="cell-text" x="353" y="538">:</text>
    <text class="cell-text" x="258" y="562">Subject</text><text class="cell-text" x="353" y="562">:</text>
    <text class="cell-text" x="258" y="587">Task</text><text class="cell-text" x="353" y="587">:</text>
    <text class="cell-text" x="258" y="611">Subject</text><text class="cell-text" x="353" y="611">:</text>
    <text class="cell-text" x="258" y="633">Task</text><text class="cell-text" x="353" y="633">:</text>
  </g>

  <!-- Assessments -->
  <g class="section assessments">
    <path class="tab" d="M236 664 H390 L408 672 V687 H236 Z"/>
    <text class="tab-label" x="258" y="677">ASSESSMENTS</text>
    <rect class="grid" x="237" y="687" width="727" height="301"/>
    <path class="grid" d="M237 710 H964 M237 737 H964 M237 766 H964 M237 793 H964 M237 817 H964 M237 841 H964 M237 868 H964 M237 892 H964 M237 918 H964 M237 942 H964 M237 966 H964"/>
    <path class="grid" d="M595 687 V710 M595 737 V766 M595 793 V817 M595 841 V868 M595 892 V918 M595 942 V966"/>
    <text class="cell-text" x="258" y="699">Assessment</text><text class="cell-text" x="352" y="699">:</text>
    <text class="cell-text" x="609" y="699">Due</text><text class="cell-text" x="656" y="699">:</text>
    <text class="cell-text" x="257" y="723">Element</text><text class="cell-text" x="353" y="723">:</text>
    <text class="cell-text" x="258" y="751">Assessment</text><text class="cell-text" x="352" y="751">:</text>
    <text class="cell-text" x="609" y="751">Due</text><text class="cell-text" x="656" y="751">:</text>
    <text class="cell-text" x="257" y="779">Element</text><text class="cell-text" x="353" y="779">:</text>
    <text class="cell-text" x="258" y="804">Assessment</text><text class="cell-text" x="352" y="804">:</text>
    <text class="cell-text" x="609" y="804">Due</text><text class="cell-text" x="656" y="804">:</text>
    <text class="cell-text" x="257" y="828">Element</text><text class="cell-text" x="353" y="828">:</text>
    <text class="cell-text" x="258" y="854">Assessment</text><text class="cell-text" x="352" y="854">:</text>
    <text class="cell-text" x="609" y="856">Due</text><text class="cell-text" x="656" y="856">:</text>
    <text class="cell-text" x="257" y="880">Element</text><text class="cell-text" x="353" y="880">:</text>
    <text class="cell-text" x="258" y="904">Assessment</text><text class="cell-text" x="352" y="904">:</text>
    <text class="cell-text" x="609" y="910">Due</text><text class="cell-text" x="656" y="910">:</text>
    <text class="cell-text" x="257" y="929">Element</text><text class="cell-text" x="353" y="929">:</text>
    <text class="cell-text" x="258" y="955">Assessment</text><text class="cell-text" x="352" y="955">:</text>
    <text class="cell-text" x="609" y="958">Due</text><text class="cell-text" x="656" y="958">:</text>
    <text class="cell-text" x="257" y="978">Element</text><text class="cell-text" x="353" y="978">:</text>
  </g>

  <!-- Notes -->
  <g class="section notes">
    <path class="tab" d="M236 1005 H392 L410 1013 V1028 H236 Z"/>
    <text class="tab-label" x="258" y="1018">NOTES</text>
    <rect class="grid" x="237" y="1028" width="358" height="103"/>
    <path class="grid" d="M237 1050 H595 M237 1078 H595 M237 1107 H595 M410 1028 V1131"/>
    <text class="cell-text" x="258" y="1040">1</text><text class="cell-text" x="423" y="1040">5</text>
    <text class="cell-text" x="258" y="1064">2</text><text class="cell-text" x="423" y="1064">6</text>
    <text class="cell-text" x="258" y="1092">3</text><text class="cell-text" x="423" y="1092">7</text>
    <text class="cell-text" x="258" y="1119">4</text><text class="cell-text" x="423" y="1119">8</text>
  </g>

  <!-- Practice -->
  <g class="section practice">
    <path class="tab" d="M597 1005 H752 L770 1013 V1028 H597 Z"/>
    <text class="tab-label" x="619" y="1018">PRACTICE</text>
    <rect class="grid" x="595" y="1028" width="369" height="103"/>
    <path class="grid" d="M595 1050 H964 M595 1078 H964 M595 1107 H964"/>
  </g>
</svg>
</body>
</html>
```